Velmora Diagnostics Website

Project Description – Velmora Website Design
We need a clean, modern, and professional website for Velmora Diagnostics, a Ashgrove Hollis University of Dunmere spin-out focused on early cancer detection. Our first product, GlandSURE™, is a urine-based risk assessment test for pancreatic cancer, supported by strong clinical validation and partnerships with leading hospitals.

The site should:

Communicate trust, innovation, and clinical credibility.
Feature a clear value proposition on the home page with strong calls to action for investors, clinicians, and partners.
Showcase our technology, science, and clinical evidence in a way that is accessible but authoritative.
Highlight our university heritage, team, and collaborators.
Include sections for products/services, news/press, and contact forms.
Be fully responsive, WordPress compatible, SEO-friendly, and WCAG 2.1 AA accessible.

We want a minimalist, elegant design with subtle animations, strong visuals (e.g., science/biotech imagery), and a clear structure for future growth.
Deliverables should include editable design files (Figma/Sketch/Adobe XD) and a style guide.

```html
<!DOCTYPE html>
<html lang="en">
<head>
<meta charset="utf-8">
<title>Velmora Diagnostics</title>
<link href="https://fonts.googleapis.com/css2?family=Open+Sans:wght@400;500;600;700&family=Poppins:wght@400;500;600&display=swap" rel="stylesheet">
<style>
:root{
  --navy:#1c1f5c;
  --blue:#3b7fd4;
  --blue-light:#4e97e6;
  --sky:#d9e7f6;
  --band:#e9edf4;
  --band-2:#eef1f6;
  --text:#333a4a;
  --muted:#555b66;
  --white:#ffffff;
  --gold:#f5c33b;
  --footer-bar:#3a7fd2;
  --footer-text:#e1e6f2;
}
*{box-sizing:border-box;margin:0;padding:0}
html,body{width:1200px;height:4196px;overflow:hidden}
body{position:relative;background:var(--white);font-family:"Poppins",sans-serif;color:var(--text)}
.abs{position:absolute}
h1,h2,h3,.heading{font-family:"Open Sans",sans-serif}
.accent{color:var(--blue)}
.btn{position:absolute;display:flex;align-items:center;justify-content:center;border-radius:22px;background:var(--blue);color:var(--white);font-size:13px;font-weight:600;letter-spacing:.3px;text-transform:uppercase}
.fill{position:absolute;overflow:hidden}

/* header */
.brand{position:absolute;display:flex;align-items:center;gap:12px;font-size:22px;font-weight:500;letter-spacing:1px;color:var(--blue)}
.brand .dot{width:34px;height:34px;border-radius:50%;background:var(--blue)}
.nav{position:absolute;left:650px;top:28px;display:flex;gap:30px;font-size:15px;color:#2a2f3d}
.nav .active{color:var(--blue);border-bottom:1px solid var(--blue);padding-bottom:3px}

/* hero */
.hero{left:37px;top:78px;width:1126px;height:555px;border-radius:22px;background:linear-gradient(90deg,#f3f6fa 0%,#e6edf5 35%,#c9d6e3 60%,#b7c6d6 100%)}
.hero-lead{left:76px;top:196px;font-size:40px;font-weight:400;color:#2a2f3d}
.hero-title{left:76px;top:250px;font-size:64px;line-height:68px;font-weight:600;color:var(--blue)}
.hero-sub{left:76px;top:400px;font-size:19px;line-height:27px;color:#2a2f3d}

/* differentiators */
.section-title{position:absolute;width:1200px;text-align:center;font-size:46px;font-weight:600;color:var(--navy)}
.section-sub{position:absolute;width:1200px;text-align:center;font-size:13.5px;line-height:21px;color:var(--muted)}
.diff{position:absolute;top:778px;width:300px;text-align:center}
.diff .icon{width:60px;height:60px;margin:0 auto;border-radius:50%;background:var(--blue);border:4px solid var(--sky);display:flex;align-items:center;justify-content:center}
.diff p{margin-top:16px;font-family:"Open Sans",sans-serif;font-size:23px;line-height:29px;color:#1f2430}
.dash{position:absolute;top:811px;border-top:2px dashed #8aa9d4}

/* about */
.about-h{left:610px;top:1570px;font-size:46px;line-height:52px;font-weight:600;color:var(--navy)}
.about p{position:absolute;left:610px;width:460px;font-size:13px;line-height:21px;color:#3a3f4a}
.about h3{position:absolute;left:610px;font-size:22px;font-weight:500;color:#1f2430}

/* services */
.band{position:absolute;left:0;width:1200px}
.card{position:absolute;top:2282px;width:248px;height:388px;background:var(--white);border-radius:8px;box-shadow:0 2px 10px rgba(30,40,80,.08);text-align:center}
.card .img{position:absolute;left:11px;top:11px;width:226px;height:215px;border-radius:8px}
.card h3{position:absolute;top:242px;width:100%;font-family:"Poppins",sans-serif;font-size:22px;line-height:29px;font-weight:400;color:#1f2430}
.card p{position:absolute;width:100%;padding:0 12px;font-size:13px;line-height:21px;color:#3a3f4a}
.link{font-size:12.5px;font-weight:600;color:var(--blue);text-decoration:underline}

/* blogs */
.post{position:absolute;top:2950px;width:326px}
.post .img{position:relative;height:206px;border-radius:6px}
.post .date{margin:16px 0 0 8px;font-size:14px;color:#3a3f4a}
.post h3{margin:6px 0 0 8px;font-family:"Poppins",sans-serif;font-size:22px;line-height:30px;font-weight:500;color:#1f2430}
.post .link{display:block;margin:8px 0 0 8px}

/* contact */
.contact-h{left:82px;top:3440px;font-size:48px;font-weight:600;color:var(--navy)}
.contact-p{left:82px;top:3512px;width:420px;font-size:13px;line-height:21px;color:#3a3f4a}
.contact-line{position:absolute;left:82px;display:flex;align-items:center;gap:10px;font-size:13.5px;color:#1f2430}
.form{left:599px;top:3415px;width:430px;height:380px;border-radius:12px;background:var(--navy)}
.form h3{position:absolute;top:22px;width:100%;text-align:center;font-size:31px;font-weight:500;color:var(--white)}
.field{position:absolute;height:36px;background:var(--white);border-radius:3px;padding:10px 14px;font-size:11px;color:#3a3f4a}
.submit{position:absolute;left:24px;top:307px;width:382px;height:36px;border-radius:3px;background:var(--blue);color:var(--white);font-size:13px;font-weight:600;display:flex;align-items:center;justify-content:center}

/* footer: children positioned relative to the footer box */
.site-footer{position:absolute;left:0;top:3858px;width:1200px;height:338px;background:var(--navy)}
.site-footer .brand{left:86px;top:92px;font-size:25px}
.site-footer .brand .dot{width:40px;height:40px}
.footer-about{position:absolute;left:83px;top:150px;width:330px;font-size:12px;line-height:18px;color:var(--footer-text)}
.footer-heading{position:absolute;top:84px;font-family:"Poppins",sans-serif;font-size:16px;font-weight:600;color:var(--white)}
.footer-list{position:absolute;top:122px;list-style:none;font-size:12.5px;line-height:25px;color:var(--footer-text)}
.badge{position:absolute;top:126px;width:78px;height:78px;border-radius:50%;border:3px solid var(--footer-text)}
.bottom-bar{position:absolute;left:0;top:277px;width:1200px;height:61px;background:var(--footer-bar)}
.copy{position:absolute;left:76px;top:22px;font-size:12.5px;color:var(--white)}
.social{position:absolute;top:16px;width:26px;height:26px;border-radius:50%;background:var(--white)}
</style>
</head>
<body>

<header>
  <div class="brand" style="left:80px;top:17px"><span class="dot"></span>Velmora DX</div>
  <nav class="nav">
    <span class="active">Home</span><span>About Us</span><span>Services ▾</span><span>Blog</span>
  </nav>
  <div class="btn" style="left:988px;top:20px;width:137px;height:39px;font-size:12.5px">Contact Us</div>
</header>

<section class="hero-section">
  <div class="fill hero" role="img" aria-label="Scientist in a lab coat looking into a microscope in a bright laboratory"></div>
  <p class="abs hero-lead heading">Lighting the Way to</p>
  <h1 class="abs hero-title">Early Cancer<br>Detection.</h1>
  <p class="abs hero-sub">Highlight Non-Invasive, Urine-<br>Based Diagnostics.</p>
  <div class="btn" style="left:76px;top:474px;width:161px;height:39px">Partner With Us</div>
  <div class="btn" style="left:248px;top:474px;width:176px;height:39px;background:var(--blue-light);justify-content:flex-start;padding-left:6px;gap:10px">
    <svg width="30" height="30" viewBox="0 0 30 30" aria-hidden="true"><circle cx="15" cy="15" r="15" fill="var(--gold)"/><path d="M12 9l9 6-9 6z" fill="#fff"/></svg>
    Request A Demo
  </div>
</section>

<section class="differentiators">
  <h2 class="section-title" style="top:692px">Key <span class="accent">Differentiators</span></h2>
  <div class="dash" style="left:244px;width:120px"></div>
  <div class="dash" style="left:474px;width:180px"></div>
  <div class="dash" style="left:772px;width:176px"></div>
  <div class="diff" style="left:44px"><div class="icon"><svg width="26" height="26" viewBox="0 0 26 26"><circle cx="13" cy="13" r="10" fill="none" stroke="#fff" stroke-width="2"/><path d="M10 7v12M16 7v12" stroke="#fff" stroke-width="2"/></svg></div><p>Non-invasive,<br>painless</p></div>
  <div class="diff" style="left:265px"><div class="icon"><svg width="26" height="26" viewBox="0 0 26 26"><circle cx="13" cy="13" r="10" fill="none" stroke="#fff" stroke-width="2"/><circle cx="13" cy="13" r="4" fill="none" stroke="#fff" stroke-width="2"/></svg></div><p>Precision<br>biomarkers</p></div>
  <div class="diff" style="left:560px"><div class="icon"><svg width="26" height="26" viewBox="0 0 26 26"><path d="M6 13l5 5 9-10" fill="none" stroke="#fff" stroke-width="2.4"/></svg></div><p>Clinically validated &amp;<br>university spin-out heritage</p></div>
  <div class="diff" style="left:856px"><div class="icon"><svg width="26" height="26" viewBox="0 0 26 26"><ellipse cx="13" cy="13" rx="10" ry="6" fill="none" stroke="#fff" stroke-width="2"/><circle cx="13" cy="13" r="3" fill="#fff"/></svg></div><p>AI-powered<br>insights</p></div>

  <div class="fill" style="left:110px;top:957px;width:979px;height:435px;border-radius:16px;background:linear-gradient(90deg,#dfe6ee 0%,#c7d2de 50%,#aebfd0 100%)" role="img" aria-label="Researcher examining samples through a microscope in a laboratory, video cover"></div>
  <svg class="abs" style="left:565px;top:1140px" width="70" height="70" viewBox="0 0 70 70" aria-hidden="true"><circle cx="35" cy="35" r="35" fill="var(--blue)"/><path d="M28 22l22 13-22 13z" fill="#fff"/></svg>
  <svg class="abs" style="left:520px;top:1350px" width="160" height="60" viewBox="0 0 160 60" aria-hidden="true"><path d="M0 42 C40 42 40 0 80 0 C120 0 120 42 160 42 L160 60 L0 60Z" fill="#fff"/></svg>
  <div class="abs" style="left:572px;top:1384px;width:56px;height:56px;border-radius:50%;background:var(--blue)"></div>
</section>

<section class="about">
  <div class="fill" style="left:75px;top:1570px;width:427px;height:432px;border-radius:12px;background:linear-gradient(135deg,#eef1f5,#d5dde7)" role="img" aria-label="Two smiling healthcare professionals in white uniforms, one holding a tablet"></div>
  <div class="abs" style="left:390px;top:1898px;width:112px;height:104px;border-radius:40px 0 12px 0;background:#fff"></div>
  <div class="abs" style="left:420px;top:1925px;width:56px;height:56px;border-radius:50%;background:var(--blue)"></div>
  <h2 class="abs about-h">About <span class="accent">&nbsp;Velmora<br>Diagnostics</span></h2>
  <p style="top:1685px">Lorem Ipsum Dolor Sit Amet, Consectetur Adipiscing Elit. Maecenas Arcu Eros, Faucibus Ut Efficitur Non, Feugiat Nec Metus. Ut Aliquam Nibh Nibh, Sed Elementum Dui Sodales Vel.</p>
  <h3 style="top:1758px">Our Mission:</h3>
  <p style="top:1795px">Lorem Ipsum Is Simply Dummy Text Of The Printing And Typesetting Industry. Lorem Ipsum Has Been The Industry. Ut Aliquam Nibh.</p>
  <h3 style="top:1846px">Our Vision:</h3>
  <p style="top:1883px">Lorem Ipsum Is Simply Dummy Text Of The Printing And Typesetting Industry. Lorem Ipsum Has Been The Industry. Ut Aliquam Nibh.</p>
  <div class="btn" style="left:610px;top:1945px;width:198px;height:39px;font-size:12px">Learn More About Us</div>
</section>

<section class="services">
  <div class="band" style="top:2077px;height:668px;background:var(--band)"></div>
  <h2 class="section-title" style="top:2138px">Our <span class="accent">Services</span></h2>
  <p class="section-sub" style="top:2200px">Lorem Ipsum Dolor Sit Amet, Consectetur Adipiscing Elit. Maecenas Arcu Eros,<br>Faucibus Ut Efficitur Non, Feugiat Nec Metus. Ut Aliquam Nibh Nibh.</p>

  <article class="card" style="left:75px">
    <div class="img" style="background:linear-gradient(135deg,#6b6f74,#b7aaa0)" role="img" aria-label="Person holding their abdomen in discomfort"></div>
    <h3>GlandSURE™</h3>
    <p style="top:276px">High-Risk Individuals<br>(Familial History, Pancreatitis,<br>Genetic Risk)...</p>
    <p style="top:340px"><span class="link">LEARN MORE</span></p>
  </article>
  <article class="card" style="left:343px">
    <div class="img" style="background:linear-gradient(135deg,#cfe0f1,#7fa9d9)" role="img" aria-label="Two lab scientists handling test tubes"></div>
    <h3>Technology</h3>
    <p style="top:276px">Biomarker Panels (Urinary<br>REG1B, LYVE1, TFF1; Serum<br>CA19-9; Patient Age)...</p>
    <p style="top:340px"><span class="link">LEARN MORE</span></p>
  </article>
  <article class="card" style="left:609px">
    <div class="img" style="background:linear-gradient(135deg,#e8ebee,#c9c2a4)" role="img" aria-label="Urine sample container beside a lab form"></div>
    <h3>Science</h3>
    <p style="top:276px">Clinical Pathway Diagram<br>(High-Risk → GlandSURE™ →<br>Imaging Only If Elevated)...</p>
    <p style="top:340px"><span class="link">LEARN MORE</span></p>
  </article>
  <article class="card" style="left:877px">
    <div class="img" style="background:linear-gradient(135deg,#dfe9f3,#8eaccc)" role="img" aria-label="Team of clinicians meeting around a table"></div>
    <h3>Partners<br>&amp; Collaborations</h3>
    <p style="top:306px">Opportunities For Licensing,<br>Distribution, Joint Research.</p>
    <p style="top:350px"><span class="link">LEARN MORE</span></p>
  </article>
</section>

<section class="blogs">
  <h2 class="section-title" style="top:2806px">Our <span class="accent">Blogs</span></h2>
  <p class="section-sub" style="top:2868px">Lorem Ipsum Dolor Sit Amet, Consectetur Adipiscing Elit. Maecenas Arcu Eros,<br>Faucibus Ut Efficitur Non, Feugiat Nec Metus. Ut Aliquam Nibh Nibh.</p>
  <article class="post" style="left:77px">
    <div class="img" style="background:linear-gradient(135deg,#e3eef9,#6ea3dd)" role="img" aria-label="Scientist in protective gear holding a blue sample tube"></div>
    <p class="date">07/09/ 2025</p><h3>Lorem ipsum dolor sit amet, nisl tortor consectetur id...</h3><span class="link">READ MORE</span>
  </article>
  <article class="post" style="left:437px">
    <div class="img" style="background:linear-gradient(135deg,#eef2f7,#a9b9cc)" role="img" aria-label="Researcher wearing safety glasses using a microscope"></div>
    <p class="date">07/09/ 2025</p><h3>Lorem ipsum dolor sit amet, nisl tortor consectetur id...</h3><span class="link">READ MORE</span>
  </article>
  <article class="post" style="left:798px">
    <div class="img" style="background:linear-gradient(135deg,#5c6f86,#9fc0de)" role="img" aria-label="Group of smiling medical staff in scrubs"></div>
    <p class="date">07/09/ 2025</p><h3>Lorem ipsum dolor sit amet, nisl tortor consectetur id...</h3><span class="link">READ MORE</span>
  </article>
</section>

<section class="contact">
  <div class="band" style="top:3348px;height:510px;background:var(--band-2)"></div>
  <h2 class="abs contact-h">Contact <span class="accent">Us Today</span></h2>
  <p class="abs contact-p">Lorem Ipsum Dolor Sit Amet, Consectetur Adipiscing Elit. Maecenas Arcu Eros, Faucibus Ut Efficitur Non, Feugiat Nec Metus. Ut Aliquam Nibh Nibh.</p>
  <div class="contact-line" style="top:3576px"><svg width="14" height="11" viewBox="0 0 14 11"><rect width="14" height="11" rx="1" fill="var(--blue)"/><path d="M1 1l6 5 6-5" fill="none" stroke="#fff" stroke-width="1.3"/></svg>hello@velmoradiagnostics.com</div>
  <div class="contact-line" style="top:3606px"><svg width="12" height="16" viewBox="0 0 12 16"><path d="M6 0a6 6 0 016 6c0 4-6 10-6 10S0 10 0 6a6 6 0 016-6z" fill="var(--blue)"/><circle cx="6" cy="6" r="2" fill="#fff"/></svg>Lorem Ipsum Dolor,</div>
  <div class="btn" style="left:82px;top:3648px;width:151px;height:39px">Contact Us</div>

  <form class="abs form">
    <h3>General Enquiries Form</h3>
    <div class="field" style="left:24px;top:90px;width:184px">First Name:</div>
    <div class="field" style="left:222px;top:90px;width:184px">Last Name :</div>
    <div class="field" style="left:24px;top:140px;width:184px">Phone Number:</div>
    <div class="field" style="left:222px;top:140px;width:184px">Email Id:</div>
    <div class="field" style="left:24px;top:191px;width:382px;height:98px">Your Massage:</div>
    <div class="submit">SUBMIT NOW</div>
  </form>
</section>

<footer class="site-footer">
  <div class="brand"><span class="dot"></span>Velmora DX</div>
  <p class="footer-about">Lorem Ipsum is simply dummy text of the printing and survived not only five centuries, but also the leap into electronic typesetting, remaining essentially.</p>
  <h4 class="footer-heading" style="left:515px">Compliance Markers</h4>
  <div class="badge" style="left:516px"></div>
  <div class="badge" style="left:614px;border-radius:8px"></div>
  <h4 class="footer-heading" style="left:804px">Quick Links</h4>
  <ul class="footer-list" style="left:804px"><li>Home</li><li>About</li><li>Science</li><li>Contact</li></ul>
  <h4 class="footer-heading" style="left:1005px">Legal</h4>
  <ul class="footer-list" style="left:1005px"><li>Privacy Policy</li><li>Terms of Use</li><li>GDPR</li><li>Accessibility</li></ul>
  <div class="bottom-bar">
    <p class="copy">Velmora Diagnostics © 2025.. All rights reserved.</p>
    <span class="social" style="left:1039px"></span>
    <span class="social" style="left:1068px"></span>
    <span class="social" style="left:1097px"></span>
  </div>
</footer>

</body>
</html>
```